Website Design for Business Law Firm

We have a logo and now we would like a web site design for our new website. Our small firm provides creative and aggressive transactional (not litigation) legal services to advise healthcare, technology, internet-based and traditional companies and investors in such companies on healthcare, technology, financing, mergers/acquisitions, real estate and other transactions, legal compliance and general corporate and business matters.

We would like to see a website design that is professional and appropriate for executives, professionals, investors and government regulators to visit, that conveys professionalism and competence while being a little edgy and modern - no typical legal motifs such as gavels, books, or scales of justice. We advise businesses and investors and guide them through complicated issues quickly, capably and differently from other law firms. We are part of the business team and get things done.

The logo is attached, and we like gray as a color to complement it. The intention of the logo is to convey that in a storm or challenging time, people come to this firm, and people come to this firm when they need the power and disruption to change things or shake them up.

I have also enclosed a picture of our business card for consideration.

On the other hand, you can check out the current simple site at www.quenlow.example to see we have used a space motif in the past to evoke that we help create stars (the nebula featured there). This is not a necessary part of the new website and it may look better without it.

We appreciate your creativity and look forward to designs.

Industry/Entity Type

Business

Requirements
Must have
• We anticipate the following pages, and you may submit different ideas for the different pages:
• 1. Landing page
• 2. Services pages - healthcare, IT/Technology, general counsel services, financings, mergers/acquisitions, mediation/arbitration, procurement and productization
• 3. About Us including contact information
• Our name and contact information:
• Quenlow Law Firm, P.C.
• 7816 SW 19th Ave.
• Portland, OR 97213
• phone: 555.614.2873
• fax: 555.730.4158
Nice to have
• Please consider designs that enhance the impressions we are looking for
Should not have
• Please no gavels, scales of justice, law books, or similar traditional legal imagery.

```html
<!DOCTYPE html>
<html lang="en">
<head>
<meta charset="utf-8">
<title>Quenlow Law Firm</title>
<link rel="stylesheet" href="https://fonts.googleapis.com/css2?family=Arimo:ital,wght@0,400;0,700;1,400&family=Open+Sans:wght@400;600&family=Tinos&display=swap">
<style>
  :root {
    --ink: #333333;
    --ink-soft: #555555;
    --rule: #3a3a3a;
    --accent: #ffb400;
    --white: #ffffff;
    --footer: #2d2d2d;
    --button-top: #6a6a6a;
    --button-bottom: #3c3c3c;
  }
  * { box-sizing: border-box; margin: 0; padding: 0; }
  html, body { width: 1200px; height: 853px; overflow: hidden; background: var(--white); }
  body { position: relative; font-family: "Arimo", Arial, sans-serif; color: var(--ink); }

  .brand { position: absolute; left: 287px; top: 0; width: 249px; height: 60px; display: flex; align-items: center; gap: 10px; }
  .brand-mark { width: 14px; height: 14px; background: var(--rule); }
  .brand-name { font-family: "Arimo", Arial, sans-serif; font-size: 32px; letter-spacing: 8px; color: var(--rule); font-weight: 400; }

  .main-nav { position: absolute; top: 28px; right: 288px; display: flex; gap: 20px; font-size: 14.5px; }
  .main-nav a { color: var(--ink); text-decoration: none; padding-bottom: 1px; }
  .main-nav a.is-current { border-bottom: 1px solid var(--ink); }

  .hero { position: absolute; left: 287px; top: 77px; width: 626px; height: 253px;
    background: linear-gradient(180deg, #6e6a64 0%, #4a4640 30%, #2a2620 55%, #1a1712 100%); }
  .hero::after { content: ""; position: absolute; inset: 0;
    background: linear-gradient(90deg, rgba(0,0,0,0) 55%, rgba(230,120,40,.55) 100%);
    -webkit-mask: linear-gradient(180deg, #000 0%, #000 40%, transparent 60%); mask: linear-gradient(180deg, #000 0%, #000 40%, transparent 60%); }

  .section-title { font-family: "Open Sans", Arial, sans-serif; font-size: 15px; font-weight: 400; color: var(--ink); }
  .intro-block { position: absolute; top: 347px; width: 186px; border-top: 2px solid var(--rule); }
  .intro-block .section-title { margin-top: -1px; }
  .intro-block--team { left: 286px; }
  .intro-block--services { left: 505px; }
  .intro-block p { font-family: "Tinos", serif; font-size: 9.5px; line-height: 10.5px; color: var(--ink); margin-top: 0; padding-left: 1px; }
  .intro-block p:first-of-type { margin-top: 22px; }
  .intro-block p + p { margin-top: 5px; }
  .more-button { display: block; margin-top: 6px; width: 53px; height: 21px; border-radius: 4px;
    background: linear-gradient(180deg, var(--button-top), var(--button-bottom));
    color: var(--white); font-size: 7px; text-align: center; line-height: 21px; text-decoration: none; }

  .news { position: absolute; left: 287px; top: 538px; width: 405px; border-top: 2px solid var(--rule); }
  .news .section-title { margin-top: -2px; }
  .news-item { position: absolute; left: 0; display: flex; gap: 10px; }
  .news-item--first { top: 33px; }
  .news-item--second { top: 146px; }
  .news-thumb { width: 93px; height: 94px; border: 1px solid #d8d8d8; flex: none; }
  .news-thumb--ribbon { background: linear-gradient(135deg, #efe3c8 0%, #c99a5a 45%, #a33428 70%, #e8d7b4 100%); }
  .news-thumb--signing { background: linear-gradient(150deg, #8a5a2e 0%, #c9935d 40%, #efe9de 75%, #d8d2c6 100%); height: 98px; }
  .news-body { width: 297px; }
  .news-date { font-family: "Arimo", Arial, sans-serif; font-size: 6.5px; margin-top: -3px; }
  .news-body p { font-family: "Tinos", serif; font-size: 9px; line-height: 10.4px; margin-top: 19px; }
  .read-more { display: block; margin-top: 6px; font-size: 6.5px; color: var(--accent); text-decoration: none; }

  .contact-card { position: absolute; left: 727px; top: 347px; width: 186px; height: 178px; background: var(--accent); color: var(--white); padding: 10px 10px; }
  .contact-card h2 { font-size: 17px; font-weight: 700; margin-top: 0; }
  .contact-card .tagline { font-size: 6.5px; color: var(--ink); margin-top: 1px; }
  .contact-card .phone { font-size: 16px; font-weight: 700; margin-top: 16px; }
  .contact-card address { font-style: normal; font-size: 8.5px; font-weight: 700; line-height: 10.5px; margin-top: 14px; }
  .contact-card .email-label { font-size: 6px; color: var(--ink); font-weight: 700; margin-top: 16px; }
  .contact-card .email { font-size: 8.5px; font-weight: 700; }
  .card-pointer { position: absolute; left: 813px; top: 525px; }

  .practice { position: absolute; left: 727px; top: 544px; width: 186px; border-top: 2px solid var(--accent); }
  .practice h2 { font-size: 15px; font-weight: 400; color: var(--accent); margin-top: -1px; }
  .practice ul { list-style: none; margin-top: 14px; }
  .practice li { font-size: 11.5px; font-style: italic; color: var(--ink-soft); height: 26px; }

  .site-footer { position: absolute; left: 0; top: 802px; width: 1200px; height: 51px; background: var(--footer); color: var(--white); }
  .site-footer .copyright { position: absolute; left: 287px; top: 19px; font-size: 6.5px; }
  .follow { position: absolute; right: 296px; top: 16px; display: flex; align-items: center; gap: 8px; font-size: 6px; }
  .follow .dot { width: 10px; height: 10px; border-radius: 50%; background: var(--white); }
  .follow span.label { margin-right: 8px; }
</style>
</head>
<body>
  <header>
    <div class="brand"><span class="brand-mark"></span><span class="brand-name">QUENLOW</span></div>
    <nav class="main-nav">
      <a href="#" class="is-current">Home</a>
      <a href="#">About Us</a>
      <a href="#">Services</a>
      <a href="#">Contact Us</a>
    </nav>
  </header>

  <div class="hero" role="img" aria-label="City skyline at dusk with lit skyscrapers and an orange sunset"></div>

  <section class="intro-block intro-block--team">
    <h2 class="section-title">Our Team</h2>
    <p>Lorem ipsum dolor sit amet, consectetuer adipiscing elit, sed diam nonummy nibh euismod tincidunt ut laoreet dolore magna aliquam erat volutpat. Ut wisi enim ad</p>
    <p>Lorem ipsum dolor sit amet, consectetuer adipiscing elit, sed diam nonummy nibh euismod tincidunt ut laoreet dolore magna aliquam erat volutpat. Ut wisi enim ad</p>
    <a href="#" class="more-button">MORE</a>
  </section>

  <section class="intro-block intro-block--services">
    <h2 class="section-title">Services</h2>
    <p>Lorem ipsum dolor sit amet, consectetuer adipiscing elit, sed diam nonummy nibh euismod tincidunt ut laoreet dolore magna aliquam erat volutpat. Ut wisi enim ad</p>
    <p>Lorem ipsum dolor sit amet, consectetuer adipiscing elit, sed diam nonummy nibh euismod tincidunt ut laoreet dolore magna aliquam erat volutpat. Ut wisi enim ad</p>
    <a href="#" class="more-button">MORE</a>
  </section>

  <section class="news">
    <h2 class="section-title">News &amp; Publications</h2>
    <article class="news-item news-item--first">
      <div class="news-thumb news-thumb--ribbon" role="img" aria-label="Documents tied with a red ribbon"></div>
      <div class="news-body">
        <div class="news-date">10-25-2014</div>
        <p>Lorem ipsum dolor sit amet, consectetuer adipiscing elit, sed diam nonummy nibh euismod tincidunt ut laoreet dolore magna aliquam erat volutpat. Ut wisi enim ad minim veniam, quis nostrud exerci tation ullamcorper suscipit lobortis nisl ut aliquip ex ea commodo consequat. Duis autem vel eum iriure dolor in hendrerit in vulputate velit</p>
        <a href="#" class="read-more">READ MORE...</a>
      </div>
    </article>
    <article class="news-item news-item--second">
      <div class="news-thumb news-thumb--signing" role="img" aria-label="Hand signing a contract with a pen"></div>
      <div class="news-body">
        <div class="news-date">10-25-2014</div>
        <p>Lorem ipsum dolor sit amet, consectetuer adipiscing elit, sed diam nonummy nibh euismod tincidunt ut laoreet dolore magna aliquam erat volutpat. Ut wisi enim ad minim veniam, quis nostrud exerci tation ullamcorper suscipit lobortis nisl ut aliquip ex ea commodo consequat. Duis autem vel eum iriure dolor in hendrerit in vulputate velit</p>
        <a href="#" class="read-more">READ MORE...</a>
      </div>
    </article>
  </section>

  <aside class="contact-card">
    <h2>Contact Us</h2>
    <div class="tagline">FOR A FREE CONSULTATION</div>
    <div class="phone">555.730.4158</div>
    <address>Quenlow Law Firm, P.C.<br>7816 SW 19th Ave.<br>Fenmore, IR 40518</address>
    <div class="email-label">EMAIL</div>
    <div class="email">dana@quenlow.example</div>
  </aside>
  <svg class="card-pointer" width="14" height="7" viewBox="0 0 14 7" aria-hidden="true"><path d="M0 0H14L7 7Z" fill="var(--accent)"/></svg>

  <section class="practice">
    <h2>Areas of Practice</h2>
    <ul>
      <li>Transaction</li>
      <li>Healthcare</li>
      <li>Technology</li>
      <li>Financing</li>
      <li>Real Estate</li>
      <li>Mergers</li>
      <li>Legal compliance</li>
    </ul>
  </section>

  <footer class="site-footer">
    <div class="copyright">© 2014 BY QUENLOW LAWYER.</div>
    <div class="follow"><span class="label">FOLLOW US:</span><span class="dot"></span><span class="dot"></span></div>
  </footer>
</body>
</html>
```